Webdesign für Raumgestalter / Interior Designer und Implementierung
Zielgruppe
Wir möchten zukünftig für Menschen «Träume in Räume» verwandeln und sind spezialisiert auf Interior Design, ReDesign Home Staging wie auch Dekorationen mit folgenden Leistungen an:
- Interior Design
- Home Styling
- Home Staging
- Dekoration
Aufgabenstellung
(Wichtig: Bitte Anforderungen und Fotos im PDF File im Anhang beachten)
Aufbau der Homepage
Homepage wird in verschiedenen Seiten/Fenster aufgebaut. Diese können oben auf der Homepage angeklickt werden. Der Aufbau ist in 5 Seiten: Home, Leistungen, Referenzen, Pakete und Preise, Kontakt
- Die Homepage sollte dann von uns gemanagt werden können. (Bspw. Plattformen oder andere Gremien, wo die Homepage einfach und ohne tiefe Informatikkenntnisse gemanagt werden kann :-).)
- Die Leistungen betreffen Templating inkl. Umsetzung (Online-Fertigstellung), ich kann bei der URL-Verknüpfung unterstützen.
1) Home
Willkommensseite, inspirierend, einladend, sollte die Besucher dazu animieren vertiefter die Detail anzuschauen.
Es soll ein Button unten ermöglichen, ins zweite Fenster «Referenzen» zu klicken. Siehe unteres Kapitel.
2) Leistungen
a. Interior Design
b. Home Styling
c. Home Staging
d. Dekoration
Hier wird der Ablauf von Projekten aufgezeigt, dieser bildet sich in:
- Planung, Designen, Realisieren
Weiterer sollen realisierte Design-Projekte von bspw. Räumen mit Fotos aufgeführt sein.
3) Referenzen
- Dieses Fenster soll das Interesse möglicher Kunden im Detail erwecken
- Es soll ein erster Termin telefonisch oder per Videocall stattfinden können
(dient zum Kennenlernen, Bedürfnisse verstehen, Ablauf aufzeigen)
4) Pakete und Preise
Hier werden die Pakete und Preise beschrieben.
Die Preise werden auf Rapportsbasis erstellt und richten sich nach Offerten und Wünschen des Kunden. Preis ist bei 80 Franken pro Stunde, das erste Beratungsgespräch wird nicht verrechnet.
Hier können Details in einer Tabelle / Preisliste erarbeitet werden:
- Private Wohnräume
o Private Wohnung
o Privates Haus
o Ferienimmobilien
- Business Einrichtungen
o Einrichtungen von Geschäften
o NestoFlat-Einrichtungen
o ReDesign für Verkauf von Immo..

```html
<!DOCTYPE html>
<html lang="de">
<head>
<meta charset="utf-8">
<title>Raumwerk – Preise und Pakete</title>
<link rel="stylesheet" href="https://fonts.googleapis.com/css2?family=Poppins:wght@500;600&family=Roboto:wght@400;500&display=swap">
<style>
  :root {
    --header-bg: #3d3d3d;
    --footer-bg: #383838;
    --white: #ffffff;
    --text-dark: #2a2a2a;
    --text-body: #3a3a3a;
    --button-grey: #b3b3b3;
    --green-top: #4e6657;
    --green-bottom: #43584a;
    --line-light: rgba(255,255,255,0.75);
    --brand-teal: #1f6f86;
    --hero-light: #f8f9fa;
    --hero-grey: #dfe2e6;
  }
  * { box-sizing: border-box; margin: 0; padding: 0; }
  html, body { width: 1081px; height: 1200px; overflow: hidden; background: var(--white); }
  body { position: relative; font-family: "Roboto", Arial, sans-serif; color: var(--text-body); }

  .site-header { position: absolute; top: 0; left: 0; width: 1081px; height: 83px; background: var(--header-bg); }
  .brand { position: absolute; left: 25px; top: 17px; width: 81px; height: 49px; background: var(--white);
           display: flex; align-items: center; justify-content: center;
           font-family: "Poppins", sans-serif; font-weight: 500; font-size: 9px; letter-spacing: 1px; color: var(--header-bg); }
  .main-nav { position: absolute; top: 35px; left: 0; width: 1081px; height: 20px; }
  .main-nav a { position: absolute; top: 0; transform: translateX(-50%); font-size: 10.5px; color: var(--white); text-decoration: none; white-space: nowrap; }
  .main-nav a.is-active { border-bottom: 1.5px solid var(--white); padding-bottom: 3px; }
  .header-button { position: absolute; left: 972px; top: 29px; width: 75px; height: 24px; background: var(--button-grey);
                   border-radius: 2px; color: var(--white); font-size: 10.5px; display: flex; align-items: center; justify-content: center; }

  .hero { position: absolute; top: 83px; left: 0; width: 1081px; height: 506px; overflow: hidden; }
  .hero-image { position: absolute; inset: 0;
                background: linear-gradient(160deg, var(--hero-light) 0%, var(--hero-light) 45%, var(--hero-grey) 100%); }
  .hero-text { position: absolute; left: 84px; top: 198px; width: 330px; }
  .hero-title { font-family: "Poppins", sans-serif; font-weight: 500; font-size: 23px; color: var(--text-dark); margin-bottom: 12px; }
  .hero-copy { font-size: 11.5px; line-height: 18px; color: var(--text-body); }
  .scroll-hint { position: absolute; left: 535px; top: 481px; }

  .offer { position: absolute; top: 589px; left: 0; width: 1081px; height: 354px;
           background: linear-gradient(180deg, var(--green-top) 0%, var(--green-top) 50%, var(--green-bottom) 100%); color: var(--white); }
  .offer-title { position: absolute; left: 116px; top: 52px; font-family: "Poppins", sans-serif; font-weight: 500; font-size: 23px; }
  .offer-list { position: absolute; left: 418px; top: 40px; width: 548px; list-style: none; }
  .offer-item { height: 72px; display: flex; align-items: center; justify-content: space-between;
                border-bottom: 1px solid var(--line-light); padding-bottom: 22px; }
  .offer-item:last-child { border-bottom: none; }
  .offer-name { font-family: "Poppins", sans-serif; font-weight: 500; font-size: 16px; }

  .site-footer { position: absolute; top: 943px; left: 0; width: 1081px; height: 166px; background: var(--footer-bg); color: var(--white); }
  .footer-contact { position: absolute; top: 52px; width: 100%; text-align: center; font-size: 10.5px; }
  .footer-contact .sep { margin: 0 8px; }
  .footer-links { position: absolute; top: 110px; width: 100%; text-align: center; font-size: 10.5px; }
  .footer-links a { color: var(--white); text-decoration: underline; margin: 0 6px; }
  .footer-contact a { color: var(--white); text-decoration: underline; }

  .platform-bar { position: absolute; top: 1109px; left: 0; width: 1081px; height: 91px; background: var(--white);
                  display: flex; justify-content: center; align-items: baseline; padding-top: 41px; font-size: 9.5px; color: var(--text-dark); gap: 8px; }
  .platform-name { font-family: "Roboto", sans-serif; font-weight: 500; font-size: 11px; color: var(--brand-teal); letter-spacing: 0.5px; }
  .platform-bar a { color: var(--text-dark); }
</style>
</head>
<body>
  <header class="site-header">
    <div class="brand">RAUMWERK</div>
    <nav class="main-nav">
      <a href="#" style="left:375px">Home</a>
      <a href="#" style="left:440px">Leistungen</a>
      <a href="#" style="left:517px">Referenzen</a>
      <a href="#" class="is-active" style="left:609px">Pakete und Preise</a>
      <a href="#" style="left:694px">Kontakt</a>
    </nav>
    <div class="header-button">Kontakt</div>
  </header>

  <section class="hero">
    <div class="hero-image" role="img" aria-label="Hell verblasstes Foto einer modernen Glasfassade eines Bürogebäudes"></div>
    <div class="hero-text">
      <h1 class="hero-title">Preise und Pakete</h1>
      <p class="hero-copy">Unsere Preise werden auf Rapportbasis verrechnet und richten sich nach Offerten und Wünschen des Kunden. Unser Stundenansatz liegt bei Fr. 80.-, das erste Beratungsgespräch ist kostenlos.</p>
    </div>
    <svg class="scroll-hint" width="10" height="6" viewBox="0 0 10 6"><polygon points="0,0 10,0 5,6" fill="#111"/></svg>
  </section>

  <section class="offer">
    <h2 class="offer-title">Unser Angebot</h2>
    <ul class="offer-list">
      <li class="offer-item"><span class="offer-name">Private Wohnräume</span><svg width="16" height="16"><path d="M8 0V16M0 8H16" stroke="#fff" stroke-width="1.3"/></svg></li>
      <li class="offer-item"><span class="offer-name">Business Einrichtungen</span><svg width="16" height="16"><path d="M8 0V16M0 8H16" stroke="#fff" stroke-width="1.3"/></svg></li>
      <li class="offer-item"><span class="offer-name">Online-Beratung per Videocall</span><svg width="16" height="16"><path d="M8 0V16M0 8H16" stroke="#fff" stroke-width="1.3"/></svg></li>
      <li class="offer-item"><span class="offer-name">Farb- und Stilberatung</span><svg width="16" height="16"><path d="M8 0V16M0 8H16" stroke="#fff" stroke-width="1.3"/></svg></li>
    </ul>
  </section>

  <footer class="site-footer">
    <p class="footer-contact"><a href="#">kontakt@raumwerk-studio.ch</a><span class="sep">·</span>079 412 56 78<span class="sep">·</span>Lindenweg 7, 6030 Seedorf</p>
    <p class="footer-links"><a href="#">Impressum</a> <a href="#">Datenschutz</a> <a href="#">Cookie-Einstellungen</a></p>
  </footer>

  <div class="platform-bar">
    <span class="platform-name">BAUKASTO</span>
    <span>Das kannst du auch! Melde dich kostenlos an bei <a href="#">https://baukasto.example/</a></span>
  </div>
</body>
</html>
```